Business Card Design Project

the following info needs to fit nicely and professionally.

logo,office address,phone,fax,cell, email address,name, title.

example: attached logo, 48310 brenner ln suite 400 poway, ca 92064
p.858.317.2950, f.858.317.2958, c.858.264.7031
email. tomas@ridgeline-asphalt.com
name.tomas valcour
title. account manager

Target Market(s)

executives, ceo's, upper management

Industry/Entity Type

Business

```html
<!DOCTYPE html>
<html lang="en">
<head>
<meta charset="UTF-8">
<title>Ridgeline Asphalt – Business Card</title>
<link rel="stylesheet" href="https://fonts.googleapis.com/css2?family=Cinzel:wght@500;600&family=Mulish:wght@600;700;800&display=swap">
<style>
  :root {
    --page-bg: #cfcfcf;
    --card-bg-center: #262626;
    --card-bg-edge: #0c0c0c;
    --ink: #ffffff;
    --accent: #f6c21a;
  }
  * { box-sizing: border-box; margin: 0; padding: 0; }
  html, body {
    width: 1200px;
    height: 900px;
    overflow: hidden;
    background: var(--page-bg);
  }
  .card {
    position: absolute;
    left: 100px;
    top: 164px;
    width: 1000px;
    height: 571px;
    background:
      radial-gradient(ellipse at 45% 40%, var(--card-bg-center) 0%, #151515 55%, var(--card-bg-edge) 100%);
    color: var(--ink);
    font-family: "Mulish", "Century Gothic", sans-serif;
    box-shadow: 0 6px 18px rgba(0,0,0,0.35);
  }
  .contact-person {
    position: absolute;
    left: 57px;
    top: 50px;
  }
  .person-name {
    font-family: "Cinzel", "Trajan Pro", serif;
    font-weight: 500;
    font-size: 40px;
    letter-spacing: 1px;
    line-height: 1;
  }
  .person-title {
    margin-top: 16px;
    font-weight: 700;
    font-size: 28px;
    line-height: 1.1;
  }
  .person-email {
    margin-top: 12px;
    font-weight: 700;
    font-size: 30px;
    line-height: 1.1;
  }
  .office-address {
    margin-top: 8px;
    font-weight: 800;
    font-size: 19px;
    line-height: 1.1;
  }
  .phone-list {
    position: absolute;
    left: 675px;
    top: 52px;
    list-style: none;
    font-weight: 800;
    font-size: 31px;
    line-height: 46px;
    letter-spacing: 0.5px;
  }
  .brand-mark {
    position: absolute;
    left: 140px;
    top: 310px;
    width: 170px;
    height: 170px;
    border-radius: 50%;
    background: var(--accent);
  }
  .brand-name {
    position: absolute;
    left: 350px;
    top: 440px;
    font-family: "Cinzel", "Trajan Pro", serif;
    font-weight: 600;
    font-size: 54px;
    line-height: 1;
    letter-spacing: 1px;
    color: var(--ink);
    white-space: nowrap;
  }
</style>
</head>
<body>
  <section class="card">
    <div class="contact-person">
      <h1 class="person-name">Tomas Valcour</h1>
      <p class="person-title">Account Manager</p>
      <p class="person-email">tomas@ridgeline-asphalt.com</p>
      <p class="office-address">48310 brenner ln suite 400 poway, ca 92064</p>
    </div>

    <ul class="phone-list">
      <li>P. 858.317.2950</li>
      <li>F. 858.317.2958</li>
      <li>C. 858.264.7031</li>
    </ul>

    <div class="brand-mark" aria-hidden="true"></div>
    <p class="brand-name">Ridgeline Asphalt</p>
  </section>
</body>
</html>
```